Lanternfield Drinks business cards

We need a business card design for our new logo. The company is modern, progressive, professional, yet approachable. The key products are ready to drink bottles and cans of coffee based beverages.
These cards will be a critical part of the first impression made by our sales organization, business development team, and all external facing personnel.
Card can be a vertical or horizontal orientation.

Target Market(s)

Customers, suppliers, business partners

Industry/Entity Type

Business

Contact Information for Business Card

Business cards should feature Company Name and Logo.

Font styles to use
Serif

Colors

Designer to choose colors to be used in the design.

Requirements
Must have
• Strong readability of Name, phone #, mobile number and email address.
• Job title, website url, Street Address, and other details can be secondary level readability.
Nice to have
• High impact, simplistic quality design.
• Ok to utilize the 'H in the box' separate from the company name

```html
<!DOCTYPE html>
<html lang="en">
<head>
<meta charset="utf-8">
<title>Lanternfield Drinks — Business Cards</title>
<link href="https://fonts.googleapis.com/css2?family=Crimson+Text:wght@400;600&display=swap" rel="stylesheet">
<style>
  :root {
    --backdrop: #3b3b3b;
    --card: #232323;
    --ink-light: #f2f2f2;
    --accent: #e05a30;
    --accent-warm: #f0a030;
    --emboss: #4a4a4a;
  }
  * { margin: 0; padding: 0; box-sizing: border-box; }
  html, body { width: 799px; height: 1200px; overflow: hidden; }
  body {
    background: var(--backdrop);
    font-family: "Crimson Text", Georgia, serif;
    position: relative;
  }
  .card {
    position: absolute;
    left: 60px;
    width: 680px;
    height: 390px;
    background: var(--card);
    border-radius: 4px;
    box-shadow: 0 12px 30px rgba(0,0,0,0.45);
    overflow: hidden;
  }
  .card--front { top: 150px; }
  .card--back { top: 660px; }

  /* Front */
  .front-mark {
    position: absolute;
    inset: 0;
    display: flex;
    align-items: center;
    justify-content: center;
    gap: 18px;
  }
  .front-mark__square {
    width: 56px; height: 56px;
    border: 6px solid var(--emboss);
  }
  .front-mark__name {
    font-size: 44px;
    font-weight: 600;
    color: var(--emboss);
    letter-spacing: 1px;
  }

  /* Back: brand */
  .brand {
    position: absolute;
    left: 30px; top: 95px;
    width: 300px;
    display: flex;
    flex-direction: column;
    align-items: center;
    gap: 14px;
  }
  .brand__square {
    width: 62px; height: 62px;
    border: 5px solid var(--accent);
  }
  .brand__name {
    font-size: 24px;
    font-weight: 600;
    color: var(--accent);
    letter-spacing: 0.5px;
    text-transform: uppercase;
    white-space: nowrap;
  }

  /* Back: contact */
  .contact {
    position: absolute;
    left: 370px; top: 95px;
    color: var(--ink-light);
  }
  .contact__name {
    font-size: 26px;
    font-weight: 600;
    color: var(--accent);
    line-height: 1;
  }
  .contact__title {
    font-size: 16px;
    font-style: italic;
    color: var(--ink-light);
    margin-top: 4px;
  }
  .contact__list {
    list-style: none;
    margin-top: 22px;
    font-size: 17px;
    line-height: 24px;
  }
  .contact__item { display: flex; align-items: center; gap: 10px; }
  .contact__icon { width: 14px; height: 14px; fill: var(--accent); flex: none; }
  .contact__address { margin-top: 6px; font-size: 17px; line-height: 22px; }

  /* Back: bands */
  .band-warm {
    position: absolute;
    left: 0; top: 300px;
    width: 300px; height: 12px;
    background: var(--accent-warm);
  }
  .band-web {
    position: absolute;
    left: 300px; top: 300px;
    width: 380px; height: 90px;
    background: var(--accent);
    border-top-left-radius: 22px;
    display: flex;
    align-items: center;
    padding-left: 40px;
  }
  .band-web__url {
    color: var(--ink-light);
    font-size: 20px;
    letter-spacing: 0.5px;
  }
</style>
</head>
<body>
  <section class="card card--front">
    <div class="front-mark">
      <div class="front-mark__square"></div>
      <div class="front-mark__name">Lanternfield</div>
    </div>
  </section>

  <section class="card card--back">
    <div class="brand">
      <div class="brand__square"></div>
      <div class="brand__name">Lanternfield Drinks</div>
    </div>

    <div class="contact">
      <div class="contact__name">Martin Hale Brooks</div>
      <div class="contact__title">Managing Director</div>
      <ul class="contact__list">
        <li class="contact__item">
          <svg class="contact__icon" viewBox="0 0 16 16"><path d="M3 1h3l1.5 4-2 1.3a9 9 0 0 0 4.2 4.2L11 8.5l4 1.5v3a2 2 0 0 1-2 2C6.5 15 1 9.5 1 3a2 2 0 0 1 2-2z"/></svg>
          555.201.3480
        </li>
        <li class="contact__item">
          <svg class="contact__icon" viewBox="0 0 16 16"><path d="M4 0h8a1 1 0 0 1 1 1v14a1 1 0 0 1-1 1H4a1 1 0 0 1-1-1V1a1 1 0 0 1 1-1zm1 2v10h6V2zm3 11a1 1 0 1 0 0 2 1 1 0 0 0 0-2z"/></svg>
          555.201.3491
        </li>
        <li class="contact__item">
          <svg class="contact__icon" viewBox="0 0 16 16"><path d="M1 3h14v10H1zm1.5 1.2V5l5.5 4 5.5-4v-.8z"/></svg>
          mbrooks@lanternfielddrinks.com
        </li>
      </ul>
      <div class="contact__address">418 Meadow Row,<br>Fairview, US 54012</div>
    </div>

    <div class="band-warm"></div>
    <div class="band-web"><span class="band-web__url">www.lanternfielddrinks.com</span></div>
  </section>
</body>
</html>
```